Bright Tooth Dentistry Business Card

We need business cards for our dental office.
We are looking for a clean, elegant design

We provide dental services to children.
Our card needs to be appealing to referring dentists, parents and our team

Target Market(s)

referring dentists, parents and our team

Industry/Entity Type

Dental Clinic

Contact Information for Business Card

4816 Juniper Lane, Suite 240
Alder Springs, OH 15237

412-837-2961 Voice
412-837-2962 fax
info@brighttoothdentalpa.com email
www.brighttoothdentalpa.com web

Font styles to use
Sans Serif

Requirements
Must have
• White background - clean, crisp, elegant, simple
• rounded corners
• different color palate - once we come up with design, we will replace the blue with orange, green,
Nice to have
• Follow our logo typeface and colors
• then we can replace color

```html
<!DOCTYPE html>
<html lang="en">
<head>
<meta charset="utf-8">
<title>Bright Tooth Dentistry – Business Card</title>
<link rel="stylesheet" href="https://fonts.googleapis.com/css2?family=Open+Sans:wght@400;600&display=swap">
<style>
  :root {
    --brand-blue: #00aeef;
    --brand-grey: #a7a9ac;
    --card-border: #b5b5b5;
    --pattern-light: #f1f1f1;
    --pattern-mid: #e4e4e4;
    --card-dark: #201f20;
    --paper: #ffffff;
    --text-light: #f2f2f2;
  }
  * { box-sizing: border-box; margin: 0; padding: 0; }
  html, body { width: 1200px; height: 1200px; overflow: hidden; background: var(--paper); }
  body { position: relative; font-family: "Open Sans", sans-serif; }

  .card {
    position: absolute;
    left: 194px;
    width: 820px;
    height: 469px;
    border-radius: 50px;
    overflow: hidden;
  }
  .card--front { top: 97px; background: var(--paper); border: 1.5px solid var(--card-border); }
  .card--back { top: 642px; background: var(--card-dark); }

  .front__pattern {
    position: absolute; left: 0; top: 0; width: 100%; height: 201px;
    background: linear-gradient(180deg, var(--pattern-mid) 0%, var(--pattern-light) 100%);
  }

  .wordmark {
    position: absolute; left: 0; right: 0;
    display: flex; align-items: center; justify-content: center; gap: 14px;
  }
  .card--front .wordmark { top: 218px; }
  .card--back .wordmark { top: 170px; }
  .wordmark__dot {
    width: 18px; height: 18px; border-radius: 50%; background: var(--brand-blue);
  }
  .wordmark__name {
    font-family: "Open Sans", sans-serif; font-weight: 600;
    font-size: 40px; color: var(--brand-blue); letter-spacing: 0; line-height: 1.2;
  }

  .front__band { position: absolute; left: 0; top: 391px; width: 100%; height: 30px; }
  .front__url {
    position: absolute; left: 0; right: 0; top: 392px; height: 28px;
    text-align: center; line-height: 28px;
    font-size: 20px; color: var(--brand-blue); letter-spacing: 0.3px;
  }

  .back__rule {
    position: absolute; left: 39px; width: 742px; top: 309px; height: 1.5px; background: var(--text-light);
  }
  .contact-list { position: absolute; left: 38px; top: 320px; list-style: none; }
  .contact-list li {
    display: flex; align-items: center; gap: 10px;
    height: 24.5px; font-size: 16px; color: var(--text-light);
  }
  .contact-list svg { width: 14px; height: 14px; fill: var(--brand-blue); }

  .address {
    position: absolute; right: 63px; top: 314px; text-align: right;
    font-size: 16px; line-height: 24.5px; color: var(--text-light); font-style: normal;
  }
  .address__icon { position: absolute; left: 763px; top: 317px; width: 18px; height: 16px; fill: var(--brand-blue); }

  .back__band { position: absolute; left: 0; top: 430px; width: 100%; height: 26px; background: var(--brand-blue); }
</style>
</head>
<body>

  <section class="card card--front" aria-label="Card front">
    <div class="front__pattern" role="img" aria-label="Soft grey damask pattern across the top of the card"></div>
    <div class="wordmark">
      <span class="wordmark__dot"></span>
      <span class="wordmark__name">Bright Tooth Dentistry</span>
    </div>
    <svg class="front__band" viewBox="0 0 820 30" preserveAspectRatio="none" aria-hidden="true">
      <g fill="var(--brand-blue)">
        <polygon points="0,0 170,0 180,30 0,30"/>
        <polygon points="172,0 182,0 193,30 183,30"/>
        <polygon points="186,0 196,0 207,30 197,30"/>
        <polygon points="200,0 210,0 221,30 211,30"/>
        <polygon points="214,0 224,0 235,30 225,30"/>
        <polygon points="597,0 605,0 595,30 587,30"/>
        <polygon points="610,0 618,0 608,30 600,30"/>
        <polygon points="623,0 631,0 621,30 613,30"/>
        <polygon points="636,0 644,0 634,30 626,30"/>
        <polygon points="650,0 820,0 820,30 640,30"/>
      </g>
    </svg>
    <p class="front__url">www.brighttoothdentalpa.com</p>
  </section>

  <section class="card card--back" aria-label="Card back">
    <div class="wordmark">
      <span class="wordmark__dot"></span>
      <span class="wordmark__name">Bright Tooth Dentistry</span>
    </div>
    <div class="back__rule"></div>
    <ul class="contact-list">
      <li>
        <svg viewBox="0 0 16 16" aria-hidden="true"><path d="M3.5 1l2.5 3-1.5 2c1 2 2.5 3.5 4.5 4.5l2-1.5 3 2.5-1.5 2.5C7 14 2 9 1 2.5z"/></svg>
        412-837-2961
      </li>
      <li>
        <svg viewBox="0 0 16 16" aria-hidden="true"><path d="M4 1h8v4H4zM1 6h14v6h-3v3H4v-3H1zM5 10v3h6v-3z"/></svg>
        412-837-2962
      </li>
      <li>
        <svg viewBox="0 0 16 16" aria-hidden="true"><path d="M1 3h14v1L8 9 1 4zM1 6l7 5 7-5v7H1z"/></svg>
        info@brighttoothdentalpa.com
      </li>
    </ul>
    <address class="address">
      4816 Juniper Lane, Suite 240<br>
      Alder Springs, OH 15237
    </address>
    <svg class="address__icon" viewBox="0 0 18 16" aria-hidden="true"><path d="M9 0l9 8h-3v8h-4v-5H7v5H3V8H0z"/></svg>
    <div class="back__band"></div>
  </section>

</body>
</html>
```